Investment firm needs refreshed corporate powerpoint slides design

We need a new and refreshed powerpoint template for our corporate investment deck. We are a technology private equity group that primarily invests in fast growing software companies and we would like to reflect that in a modern and light blue / transparant / white powerpoint and fonts template. I have also attached our old investor deck as a guideline and also check out our website to get an idea of what we do and what type of companies we invested in. Please note that our website is old and so our presentation should be a refreshed "2017" modern design, not a copy / paste of our website design and graphics.
Updates

Project Deadline Extended Reason: I'm extending the deadline to February 27, but we would ideally receive something by the end of this week.Please submit updates. Thanks Added Tuesday, February 21, 2017

Target Market(s)

Investors such as high net worth individuals, pension funds, banks, financial advisors

Industry/Entity Type

Investment

Colors
33a6d7
85cae6
cfeae6
edf8f6
ffffff
fff3d1
86cfc6

Requirements
Must have
• We let you be creative, we trust you have seen more investment presentations before.
Nice to have
• Pre-built models, flow charts, graphs, charts, etc.
Should not have
• Fancy or edgy images, this has to be a modern, fresh and trustworthy looking powerpoint template. No stock images, if you do use stock images for background purposes please be creative! :-)

```html
<!DOCTYPE html>
<html lang="en">
<head>
<meta charset="utf-8">
<title>HV Growth Equity – Investor Deck Template</title>
<link href="https://fonts.googleapis.com/css2?family=Open+Sans:wght@400;600;700&family=Roboto+Slab:wght@400;700&display=swap" rel="stylesheet">
<style>
  :root{
    --navy:#14305f;
    --navy-deep:#0c2145;
    --mid-blue:#1d4a86;
    --sky:#33a6d7;
    --sky-light:#85cae6;
    --cyan:#22d0fb;
    --ocean:#0a72b8;
    --gold:#f6c21c;
    --grey:#c9cfd6;
    --white:#ffffff;
    --sans:'Open Sans', Arial, sans-serif;
    --slab:'Roboto Slab', Georgia, serif;
  }
  *{margin:0;padding:0;box-sizing:border-box}
  html,body{width:1053px;height:1200px;overflow:hidden;background:#000}
  .board{position:relative;width:1053px;height:1200px;background:#000}
  .slide{position:absolute;overflow:hidden}
  .brand{position:absolute;font-family:var(--slab);font-weight:400;color:var(--navy)}
  .date{position:absolute;font-family:var(--sans);font-weight:700;color:var(--navy-deep)}

  /* Cover */
  .cover{left:0;top:0;width:1053px;height:593px;
    background:radial-gradient(ellipse 75% 95% at 50% 0%, #a4e6ff 0%, #52bbea 35%, #2a93d2 65%, #1a73b8 100%)}
  .cover .brand{left:16px;top:2px;font-size:38px}
  .cover-arrow{position:absolute;left:256px;top:157px}
  .title-panel{position:absolute;left:303px;top:174px;width:509px;height:100px;border-radius:12px;
    border:2px solid #e8f4fb;
    background:linear-gradient(90deg,#3d6fad 0%,#1f4884 40%,#0f2650 100%);
    display:flex;align-items:flex-end;padding:0 0 12px 24px}
  .title-panel h1{font-family:var(--slab);font-weight:700;font-size:40px;letter-spacing:1px;color:var(--white)}
  .cover-sub{position:absolute;left:256px;width:557px;text-align:center;font-family:var(--sans);font-weight:600;color:var(--mid-blue)}
  .cover-sub.one{top:283px;font-size:22px}
  .cover-rule{position:absolute;left:256px;top:315px;width:557px;height:1px;background:#e9f6fc}
  .cover-sub.two{top:325px;font-size:22px}
  .cover .date{right:18px;top:556px;font-size:19px;color:var(--white)}

  /* Section divider */
  .divider{left:0;top:604px;width:521px;height:292px;
    background:radial-gradient(ellipse 60% 65% at 50% 52%, var(--cyan) 0%, #14a7e2 55%, var(--ocean) 100%)}
  .top-strip{position:absolute;left:0;top:0;width:100%;height:20px;
    background:linear-gradient(90deg,#4f8bc4 0%,#a9cde7 55%,#f2f7fb 85%,#ffffff 100%)}
  .corner{position:absolute;left:0;top:0}
  .pill{position:absolute;left:166px;top:122px;width:201px;height:37px;border-radius:10px;
    background:linear-gradient(180deg,#2a7ee0 0%,#1450b0 100%);box-shadow:0 1px 3px rgba(0,0,0,.3);
    font-family:var(--sans);font-size:18px;color:var(--white);display:flex;align-items:center;justify-content:center;letter-spacing:.5px}
  .footer-white{position:absolute;left:0;bottom:0;width:100%;height:25px;background:var(--white)}
  .footer-white .brand,.footer-blue .brand{left:8px;top:-2px;font-size:21px}
  .footer-white .date,.footer-blue .date{right:10px;top:7px;font-size:10px}

  /* Rings slide */
  .rings{left:532px;top:604px;width:521px;height:292px;background:#2f8fc6}
  .rings-header{position:absolute;left:0;top:0;width:100%;height:67px;
    background:linear-gradient(180deg,#8aa3bc 0%,#5b86ad 22%,#2a6d9e 23%,#2b6f9f 100%)}
  .slide-title{position:absolute;right:30px;font-family:var(--slab);font-weight:700;color:var(--white);text-decoration:underline;text-decoration-thickness:2px;text-underline-offset:4px}
  .rings .slide-title{top:2px;font-size:34px}
  .rings-body{position:absolute;left:0;top:67px;width:100%;height:162px;background:var(--sky)}
  .rings-svg{position:absolute;left:0;top:67px}
  .footer-blue{position:absolute;left:0;bottom:0;width:100%;height:25px;background:linear-gradient(180deg,#2e78bb,#1b56a0)}
  .rings .footer-blue .date{color:var(--white)}

  /* Bar chart slide */
  .bars{left:0;top:906px;width:521px;height:294px;background:linear-gradient(180deg,#f2f8fd 0%,#d4e8f6 60%,#7fb2d8 100%)}
  .bars-header{position:absolute;left:0;top:0;width:100%;height:40px;
    background:linear-gradient(180deg,#a9c1d6 0%,#5e8fbd 55%,#88b6dc 100%)}
  .bars .slide-title{top:0;font-size:32px;font-variant:small-caps;right:36px}
  .bars-svg{position:absolute;left:0;top:40px}
  .bars .footer-blue{background:linear-gradient(180deg,#bfe0f6,#9ccbed)}

  /* Agenda slide */
  .agenda{left:532px;top:906px;width:521px;height:294px}
  .agenda-photo{position:absolute;inset:0;background:radial-gradient(ellipse 70% 70% at 50% 45%, #3f7d97 0%, #1f4b66 45%, #0e2337 100%)}
  .agenda-header{position:absolute;left:0;top:0;width:100%;height:40px;
    background:linear-gradient(180deg,rgba(170,190,210,.9) 0%,rgba(60,110,160,.85) 60%,rgba(40,80,130,.6) 100%)}
  .agenda .slide-title{top:0;font-size:32px;font-variant:small-caps;right:34px}
  .agenda-list{position:absolute;left:160px;top:72px;list-style:none}
  .agenda-list li{position:relative;width:195px;height:34px;margin-bottom:7px;
    background:linear-gradient(90deg,rgba(30,70,140,.85),rgba(25,60,125,.95));
    font-family:var(--slab);font-weight:700;font-size:12.5px;color:var(--gold);
    display:flex;align-items:center;justify-content:center;padding-left:12px}
  .agenda-list li::before{content:"";position:absolute;left:0;top:0;border-style:solid;border-width:17px 0 17px 14px;border-color:transparent transparent transparent rgba(200,215,235,.55)}
  .agenda .footer-clear{position:absolute;left:0;bottom:0;width:100%;height:25px}
  .agenda .footer-clear .brand{left:8px;top:-2px;font-size:21px;color:#2b5ba0}
</style>
</head>
<body>
<main class="board">

  <!-- Cover -->
  <section class="slide cover">
    <div class="brand">Halvern</div>
    <svg class="cover-arrow" width="60" height="145" viewBox="0 0 60 145">
      <polygon points="0,0 60,60 0,145" fill="#d4d8dd"/>
    </svg>
    <div class="title-panel"><h1>HV GROWTH EQUITY</h1></div>
    <p class="cover-sub one">INTRODUCTION TO TEAM AND TRACK RECORD</p>
    <div class="cover-rule"></div>
    <p class="cover-sub two">FOR US INVESTORS</p>
    <div class="date">February 17</div>
  </section>

  <!-- Section divider -->
  <section class="slide divider">
    <div class="top-strip"></div>
    <svg class="corner" width="22" height="40" viewBox="0 0 22 40"><polygon points="0,0 22,20 0,40" fill="#14305f"/></svg>
    <div class="pill">PRODUCT MARKET</div>
    <footer class="footer-white">
      <span class="brand">Halvern</span>
      <span class="date">February 17</span>
    </footer>
  </section>

  <!-- Ring statistics -->
  <section class="slide rings">
    <div class="rings-header"></div>
    <svg class="corner" width="22" height="40" viewBox="0 0 22 40"><polygon points="0,0 22,20 0,40" fill="#14305f"/></svg>
    <h2 class="slide-title">Data Analysis</h2>
    <div class="rings-body"></div>
    <svg class="rings-svg" width="521" height="162" viewBox="0 0 521 162" font-family="Open Sans, sans-serif">
      <g fill="none" stroke-width="6" stroke-dasharray="5 3.2">
        <circle cx="110" cy="76" r="44" stroke="#1f3f7a"/>
        <circle cx="110" cy="76" r="44" stroke="#f6cf3a" pathLength="100" stroke-dasharray="70 30" transform="rotate(-90 110 76)" style="stroke-dasharray:none" opacity="0"/>
        <circle cx="262" cy="76" r="44" stroke="#1f3f7a"/>
        <circle cx="413" cy="76" r="44" stroke="#1f3f7a"/>
      </g>
      <!-- coloured arcs over navy rings -->
      <g fill="none" stroke-width="6" stroke-dasharray="5 3.2">
        <path d="M110 32 A44 44 0 1 1 68.2 89.6" stroke="#f6cf3a"/>
        <path d="M262 32 A44 44 0 1 1 226.3 101.9" stroke="#f03a1c" transform="rotate(-135 262 76) rotate(110 262 76)"/>
        <path d="M413 32 A44 44 0 0 0 370.2 65.9" stroke="#36c23c" transform="rotate(-60 413 76) rotate(40 413 76)"/>
      </g>
      <g fill="#ffffff" font-size="12" text-anchor="middle">
        <text x="110" y="74">70%</text><text x="110" y="91">Study 1</text>
        <text x="262" y="74">62%</text><text x="262" y="91">Study 2</text>
        <text x="413" y="74">38%</text><text x="413" y="91">Study 3</text>
      </g>
    </svg>
    <footer class="footer-blue">
      <span class="brand" style="color:#1c3d6e">Halvern</span>
      <span class="date">February 17</span>
    </footer>
  </section>

  <!-- Bar chart -->
  <section class="slide bars">
    <div class="bars-header"></div>
    <h2 class="slide-title">Data Analysis</h2>
    <svg class="bars-svg" width="521" height="230" viewBox="0 0 521 230" font-family="Roboto Slab, serif">
      <rect x="87" y="26" width="371" height="162" fill="#dcebf6" stroke="#3a78c4" stroke-width="1.5"/>
      <g stroke="#a9cbe6" stroke-width="1">
        <line x1="87" y1="42.2" x2="458" y2="42.2"/><line x1="87" y1="58.4" x2="458" y2="58.4"/>
        <line x1="87" y1="74.6" x2="458" y2="74.6"/><line x1="87" y1="90.8" x2="458" y2="90.8"/>
        <line x1="87" y1="107" x2="458" y2="107"/><line x1="87" y1="123.2" x2="458" y2="123.2"/>
        <line x1="87" y1="139.4" x2="458" y2="139.4"/><line x1="87" y1="155.6" x2="458" y2="155.6"/>
        <line x1="87" y1="171.8" x2="458" y2="171.8"/>
      </g>
      <g font-size="11" fill="#1b1b1b" text-anchor="end">
        <text x="76" y="30">5</text><text x="76" y="46">4.5</text><text x="76" y="62">4</text>
        <text x="76" y="78">3.5</text><text x="76" y="95">3</text><text x="76" y="111">2.5</text>
        <text x="76" y="127">2</text><text x="76" y="143">1.5</text><text x="76" y="159">1</text>
        <text x="76" y="176">0.5</text><text x="76" y="192">0</text>
      </g>
      <!-- arrows: value v → top y = 188 - v*32.4 -->
      <g fill="#f3c31a">
        <rect x="121" y="61" width="6" height="127"/><polygon points="112,67 124,48 136,67"/>
        <rect x="214" y="124" width="6" height="64"/><polygon points="206,130 217,114 228,130"/>
        <rect x="307" y="92" width="6" height="96"/><polygon points="299,98 310,82 321,98"/>
        <rect x="400" y="56" width="6" height="132"/><polygon points="391,62 403,42 415,62"/>
      </g>
      <g fill="#1f3f74">
        <rect x="140" y="124" width="6" height="64"/><polygon points="132,130 143,114 154,130"/>
        <rect x="232" y="60" width="6" height="128"/><polygon points="223,66 235,46 247,66"/>
        <rect x="325" y="136" width="6" height="52"/><polygon points="317,142 328,128 339,142"/>
        <rect x="418" y="109" width="6" height="79"/><polygon points="410,115 421,99 432,115"/>
      </g>
      <g font-size="11" font-weight="700" fill="#1b1b1b" text-anchor="middle">
        <text x="133" y="210">Investor 1</text><text x="225" y="210">Investor 2</text>
        <text x="318" y="210">Investor 3</text><text x="411" y="210">Investor 4</text>
      </g>
    </svg>
    <footer class="footer-blue">
      <span class="brand">Halvern</span>
      <span class="date">February 17</span>
    </footer>
  </section>

  <!-- Agenda -->
  <section class="slide agenda">
    <div class="agenda-photo" role="img" aria-label="Soft-focus background photo of dark glossy spheres in teal and navy tones"></div>
    <div class="agenda-header"></div>
    <svg class="corner" width="22" height="40" viewBox="0 0 22 40"><polygon points="0,0 22,20 0,40" fill="#14305f"/></svg>
    <h2 class="slide-title">Agenda</h2>
    <ul class="agenda-list">
      <li>EXECUTIVE SUMMARY</li>
      <li>DIFFERENTIATED MODEL</li>
      <li>TRACK RECORD</li>
      <li>SUMMARY OF TERMS</li>
      <li>APPENDIX</li>
    </ul>
    <footer class="footer-clear">
      <span class="brand">Halvern</span>
    </footer>
  </section>

</main>
</body>
</html>
```